Fixed price car insurance banner ad for insurance broker

We need a banner ad for addition to web pages and which will advertise an innovative insurance product we are selling.

We are an insurance broker and our product is a fixed price car insurance product.

The banner ad needs to display the company logo. This will be uploaded within the file upload section.

The remainder of the banner ad needs to explain what we are offering and also include the gear stick picture for impact.

We would like to see colours that tie in with the corporate colours, or alternative are striking and have presence on even the busiest web page I.e. Black banner and silver / white text. Please see the file upload for a sample of the brochure we are preparing for this product.

Target Market(s)

Private and commercial clients with both regular and high value motor vehicles.

Industry/Entity Type

Car Insurance

Font styles to use
Serif
Sans Serif

Colors

Designer to choose colors to be used in the design.

Requirements
Must have
• The banner must have the company logo on both pages.

I would like the advert to scroll / roll / fade or other between two pages displaying the following text:

Page 1
"Motor Insurance Scheme"
"Anything But Standard"
and including the gear knob picture

Page 2
Any Driver, Any Car, No Forms and One Flat Premium*

On clicking the banner ad, this will open an email, pre populated with email contact to request more detail.

Nice to have
• Open to your suggestions on this
Should not have
• Nothing at this stage. I will guide you when the ads are being submitted.

```html
<!DOCTYPE html>
<html lang="en">
<head>
<meta charset="utf-8">
<title>Halden Insurance – Motor Insurance Scheme Banners</title>
<link href="https://fonts.googleapis.com/css2?family=Montserrat:ital,wght@0,500;0,600;1,500&display=swap" rel="stylesheet">
<style>
  :root {
    --canvas-grey: #6b6c6e;
    --banner-black: #141414;
    --banner-edge: #c9c9c9;
    --brand-white: #ffffff;
    --brand-navy: #1c2a5e;
    --accent-orange: #f5a100;
    --text-white: #ffffff;
    --metal-light: #c9ccd0;
    --metal-dark: #2a2b2d;
  }
  * { margin: 0; padding: 0; box-sizing: border-box; }
  html, body {
    width: 1200px;
    height: 800px;
    overflow: hidden;
    background: var(--canvas-grey);
    font-family: "Montserrat", Arial, sans-serif;
  }
  .stage {
    position: relative;
    width: 1200px;
    height: 800px;
  }
  .banner {
    position: absolute;
    left: 116px;
    width: 968px;
    height: 119px;
    background: var(--banner-black);
    border: 1px solid var(--banner-edge);
    overflow: hidden;
  }
  .banner--page-one { top: 233px; }
  .banner--page-two { top: 396px; }

  .brand-panel {
    position: absolute;
    left: 0;
    top: 0;
    width: 250px;
    height: 100%;
    background: var(--brand-white);
    display: flex;
    align-items: center;
    padding-left: 18px;
  }
  .brand-name {
    color: var(--brand-navy);
    font-weight: 600;
    font-size: 19px;
    letter-spacing: 0.06em;
    line-height: 1.25;
    text-transform: uppercase;
  }
  .brand-divider {
    position: absolute;
    left: 226px;
    top: 0;
    width: 40px;
    height: 100%;
  }
  .gear-photo {
    position: absolute;
    right: 0;
    top: 0;
    width: 247px;
    height: 100%;
    background:
      radial-gradient(ellipse at 55% 50%, var(--metal-light) 0%, #9a9da2 40%, transparent 75%),
      linear-gradient(90deg, var(--banner-black) 0%, var(--metal-dark) 30%, #5b5d60 100%);
  }
  .message {
    position: absolute;
    top: 0;
    height: 100%;
    display: flex;
    flex-direction: column;
    justify-content: center;
    color: var(--text-white);
  }
  .banner--page-one .message { left: 289px; gap: 8px; }
  .banner--page-two .message { left: 279px; gap: 12px; }

  .headline {
    color: var(--accent-orange);
    font-weight: 500;
    font-size: 29px;
    line-height: 1;
  }
  .tagline {
    font-style: italic;
    font-weight: 500;
    font-size: 22px;
    letter-spacing: 0.04em;
    line-height: 1;
  }
  .offer-line {
    font-weight: 500;
    font-size: 24px;
    line-height: 1;
  }
  .offer-highlight {
    color: var(--accent-orange);
  }
</style>
</head>
<body>
<main class="stage">

  <section class="banner banner--page-one" aria-label="Motor insurance banner, page one">
    <div class="brand-panel">
      <span class="brand-name">Halden<br>Insurance</span>
    </div>
    <svg class="brand-divider" viewBox="0 0 40 119" preserveAspectRatio="none" aria-hidden="true">
      <path d="M24 0 L40 0 L40 119 L12 119 Q26 60 24 0 Z" fill="var(--banner-black)"/>
      <path d="M16 0 L26 0 Q29 60 14 119 L4 119 Q19 60 16 0 Z" fill="var(--accent-orange)"/>
    </svg>
    <div class="message">
      <p class="headline">Motor Insurance Scheme</p>
      <p class="tagline">Anything But Standard</p>
    </div>
    <div class="gear-photo" role="img" aria-label="Close-up photo of a chrome gear stick gate"></div>
  </section>

  <section class="banner banner--page-two" aria-label="Motor insurance banner, page two">
    <div class="brand-panel">
      <span class="brand-name">Halden<br>Insurance</span>
    </div>
    <svg class="brand-divider" viewBox="0 0 40 119" preserveAspectRatio="none" aria-hidden="true">
      <path d="M24 0 L40 0 L40 119 L12 119 Q26 60 24 0 Z" fill="var(--banner-black)"/>
      <path d="M16 0 L26 0 Q29 60 14 119 L4 119 Q19 60 16 0 Z" fill="var(--accent-orange)"/>
    </svg>
    <div class="message">
      <p class="offer-line">Any Driver, Any Car, No Forms</p>
      <p class="offer-line">and <span class="offer-highlight">ONE FLAT PREMIUM</span></p>
    </div>
    <div class="gear-photo" role="img" aria-label="Close-up photo of a chrome gear stick gate"></div>
  </section>

</main>
</body>
</html>
```